Communication of Recommended Belief Letter

To Whom This May Concern,

My company's name is Brookfane LLC. I would like to send electronic messages to my clients. Therefore, I would like PixelForge to create a letterhead template to say Brookfane- without the LLC. My messages could extend up to 20 pages long. I would like something that is chic, fancy, and has creative designs. The background color should be white. The creative designs are open for suggestions without color restrictions. Font type and color are also open for suggestions. It may be what you believe best suite's the letterhead. I would like the letterhead to include the company logo. Please see attachment for file. Thank you.

Target Market(s)

working class American's

Industry/Entity Type

Communication

Contact Information for Business Card

The business card should be chic and fancy.

Font styles to use
Script

Requirements
Must have
• Company name: Brookfane LLC
• Company symbol: Please see attachment
• Name: Moriel Haskins
• Title: President
• Company website: www.brookfanellc-example.com
Nice to have
• Open for suggestions

```html
<!DOCTYPE html>
<html lang="en">
<head>
<meta charset="UTF-8">
<title>Brookfane Letterhead</title>
<link rel="stylesheet" href="https://fonts.googleapis.com/css2?family=Cinzel:wght@400&family=Crimson+Text:wght@400&family=Open+Sans:wght@400;600&display=swap">
<style>
  :root {
    --paper: #ffffff;
    --bronze: #b07a12;
    --brand-gold: #a8801f;
    --footer-gold: #e0a100;
    --rule-grey: #dcdcdc;
    --ink-grey: #555555;
    --footer-ink: #ffffff;
  }
  * { margin: 0; padding: 0; box-sizing: border-box; }
  html, body {
    width: 950px;
    height: 1200px;
    overflow: hidden;
    background: var(--paper);
  }
  .letterhead {
    position: relative;
    width: 950px;
    height: 1200px;
    background: var(--paper);
  }
  .top-band {
    position: absolute;
    left: 0; top: 0;
    width: 100%;
    height: 18px;
    background: var(--bronze);
  }
  .brand {
    position: absolute;
    left: 60px;
    top: 62px;
    display: flex;
    align-items: center;
    gap: 16px;
  }
  .brand-dot {
    width: 46px;
    height: 46px;
    border-radius: 50%;
    background: var(--brand-gold);
  }
  .brand-name {
    font-family: "Cinzel", serif;
    font-weight: 400;
    font-size: 40px;
    letter-spacing: 1px;
    color: var(--brand-gold);
    line-height: 1;
  }
  .signatory {
    position: absolute;
    left: 711px;
    top: 50px;
    font-family: "Crimson Text", serif;
    font-size: 21px;
    line-height: 28px;
    color: var(--ink-grey);
  }
  .header-rule {
    position: absolute;
    left: 57px;
    top: 126px;
    width: 795px;
    height: 1px;
    background: var(--rule-grey);
  }
  .body-area {
    position: absolute;
    left: 57px;
    top: 150px;
    width: 795px;
    height: 1000px;
  }
  .footer-band {
    position: absolute;
    left: 0;
    bottom: 0;
    width: 100%;
    height: 31px;
    background: var(--footer-gold);
    display: flex;
    align-items: center;
    justify-content: center;
    font-family: "Open Sans", sans-serif;
    font-size: 13px;
    color: var(--footer-ink);
    letter-spacing: -0.2px;
    white-space: nowrap;
  }
  .footer-band .label-lead { font-size: 15px; margin-right: 4px; }
  .footer-band .gap { margin-left: 6px; }
</style>
</head>
<body>
  <main class="letterhead">
    <div class="top-band"></div>

    <header>
      <div class="brand">
        <div class="brand-dot"></div>
        <span class="brand-name">BROOKFANE</span>
      </div>
      <div class="signatory">
        <div class="signatory-name">Moriel Haskins</div>
        <div class="signatory-title">President</div>
      </div>
      <div class="header-rule"></div>
    </header>

    <section class="body-area"></section>

    <footer class="footer-band">
      <span class="label-lead">Address:</span>
      <span>Alder Cove, Maryland 20977 Telephone: 555-214-7390 Fax: 555-860-4127</span>
      <span class="gap">Email: office@brookfane</span>
    </footer>
  </main>
</body>
</html>
```